Natural Skincare brand needs new labels!

We are a natural and organic skin care brand based in the united states. We are looking for unique product label designs that will help our brand stand out. We want the labels to look elegant and natural, but also incorporate some color. We want a design aspect like a line drawing on the labels, see examples. Please refer to our website to see our current labels and to get more of a feel of who we are. Our logo is included. We are looking for 5 labels for 5 different Products.
1. Body butter: 1.5"x9" rectangle wrap around 12oz jar with black lid
2. Eczema Salve: 1.5" circle silver metal tin
3. Glow Serum: 1.5"x3" rectangle Blue Dropper Bottle with black top
4. Mineral Mist: 1.5"x3" clear glass sprayer bottle (want clear label)
website: www.velmirabotanics.com
Instagram: @velmirabotanics

```html
<!DOCTYPE html>
<html lang="en">
<head>
<meta charset="utf-8">
<title>Velmira Skin Body Butter Wrap Label</title>
<link rel="stylesheet" href="https://fonts.googleapis.com/css2?family=Open+Sans:wght@400;600&family=Marcellus&family=Oswald:wght@300;400&display=swap">
<style>
  :root {
    --backdrop: #d9d6d4;
    --label-orange: #d4956a;
    --salmon: #e07a6f;
    --salmon-light: #ec9d94;
    --bronze: #b47a4f;
    --bronze-light: #d2a07a;
    --ink: #4a4545;
    --white: #ffffff;
    --lavender: #8f7fc4;
    --sprig: #6e5a52;
  }
  * { box-sizing: border-box; margin: 0; padding: 0; }
  html, body { width: 1200px; height: 900px; overflow: hidden; }
  body {
    background: var(--backdrop);
    font-family: "Open Sans", Arial, sans-serif;
    display: flex;
    align-items: center;
    justify-content: center;
  }
  .wrap-label {
    position: relative;
    width: 1120px;
    height: 214px;
    background: var(--label-orange);
    display: flex;
  }
  .info-panel {
    flex: 1;
    display: flex;
    flex-direction: column;
    align-items: center;
    justify-content: center;
    text-align: center;
    gap: 4px;
  }
  .info-heading {
    color: var(--ink);
    font-weight: 600;
    font-size: 11px;
    margin-top: 6px;
  }
  .info-text {
    color: var(--white);
    font-size: 11px;
    line-height: 1.15;
  }
  .social-row { display: flex; gap: 6px; margin: 2px 0; }
  .social-dot {
    width: 20px; height: 20px; border-radius: 50%;
    background: var(--white);
  }
  .front-panel {
    position: relative;
    width: 440px;
    height: 100%;
    overflow: hidden;
  }
  .front-top {
    position: absolute; inset: 0 0 auto 0; height: 96px;
    background: linear-gradient(90deg, var(--salmon) 0%, var(--salmon-light) 35%, var(--salmon) 75%);
    display: flex; align-items: center; justify-content: center;
  }
  .brand-mark { display: flex; align-items: center; gap: 8px; }
  .brand-dot { width: 16px; height: 16px; border-radius: 50%; background: var(--white); }
  .brand-name {
    color: var(--white);
    font-weight: 600;
    font-size: 30px;
    letter-spacing: 1px;
  }
  .front-bottom {
    position: absolute; inset: 96px 0 0 0;
    background: linear-gradient(90deg, var(--bronze) 0%, var(--bronze-light) 40%, var(--bronze) 85%);
  }
  .leaf-drawing {
    position: absolute;
    right: -70px; top: 14px;
    width: 190px; height: 190px;
    border-radius: 50%;
    background: radial-gradient(circle, rgba(150,95,60,0.35), rgba(150,95,60,0) 70%);
  }
  .product-title {
    position: absolute; left: 60px; right: 60px; top: 10px;
    border-top: 1.5px solid var(--white);
    border-bottom: 1.5px solid var(--white);
    text-align: center;
    font-family: "Marcellus", Georgia, serif;
    color: var(--white);
    font-size: 40px;
    line-height: 1.15;
    padding: 2px 0 0;
  }
  .product-size {
    position: absolute; left: 0; right: 0; top: 70px;
    text-align: center;
    font-family: "Oswald", Arial, sans-serif;
    font-weight: 300; font-size: 14px; color: var(--ink);
  }
  .product-benefits {
    position: absolute; left: 120px; right: 40px; top: 88px;
    text-align: center;
    font-family: "Oswald", Arial, sans-serif;
    font-weight: 300; font-size: 12px; line-height: 1.2; color: var(--ink);
  }
  .scent-name {
    position: absolute; left: 10px; bottom: 10px;
    font-family: "Oswald", Arial, sans-serif;
    font-weight: 300; font-size: 16px; color: var(--white);
    border-bottom: 3px solid var(--lavender);
    padding: 0 44px 0 4px;
  }
  .sprig-drawing {
    position: absolute; left: 82px; bottom: 10px;
    width: 26px; height: 44px;
    background: linear-gradient(180deg, rgba(110,90,82,0.15), rgba(110,90,82,0.55));
    border-radius: 12px 12px 2px 2px;
  }
</style>
</head>
<body>
  <section class="wrap-label">
    <div class="info-panel info-panel--left">
      <h2 class="info-heading">Ingredients :</h2>
      <p class="info-text">Lorem ipsum dolor sit<br>amet, consectetuer<br>adipiscing elit, sed diam</p>
      <h2 class="info-heading">Lorem ipsum :</h2>
      <p class="info-text">Lorem ipsum dolor sit<br>amet, consectetuer<br>adipiscing elit, sed diam<br>nonummy nibh euismod</p>
    </div>

    <div class="front-panel">
      <div class="front-top">
        <div class="brand-mark">
          <span class="brand-dot"></span>
          <span class="brand-name">Velmira Skin</span>
        </div>
      </div>
      <div class="front-bottom">
        <div class="leaf-drawing" role="img" aria-label="Fine line drawing of tropical leaves"></div>
        <h1 class="product-title">Body Butter</h1>
        <p class="product-size">12 oz</p>
        <p class="product-benefits">Moisturizing + Nourishing<br>+ Sensitive + Dry Skin</p>
        <p class="scent-name">Lavender</p>
        <div class="sprig-drawing" role="img" aria-label="Line drawing of a lavender sprig"></div>
      </div>
    </div>

    <div class="info-panel info-panel--right">
      <h2 class="info-heading">How to use :</h2>
      <p class="info-text">Lorem ipsum dolor sit<br>amet, consectetuer<br>adipiscing elit, sed diam</p>
      <h2 class="info-heading">Follow us :</h2>
      <div class="social-row">
        <span class="social-dot"></span>
        <span class="social-dot"></span>
        <span class="social-dot"></span>
      </div>
      <p class="info-text">@velmirabotanics<br>www.velmirabotanics.com</p>
    </div>
  </section>
</body>
</html>
```